Landing Page für B2B-Softwareentwicklungsfirma
Zielgruppe
Wir sind eine (relativ kleine) B2B Softwareentwicklungsfirma, die Software zum Wetten auf Pferderennen erstellt.
Unsere Kunden sind Buchmacher und Rennbahnbetreiber.
Unsere Software läuft auf verschiedener Hardware (Touchscreen Terminals, Handy, Kassa, Webseite,...) und wird teilweise von Endkunden (Sportwetter) als auch Kunden-Mitarbeitern verwendet.
Was uns von anderen Softwarefirmen in diesem Bereich unterscheidet ist:
- Wir sind extrem verlässlich und unsere Software läuft störungsfrei
- Wir haben extrem viel Knowhow und ein großes Netzwerk im Bereich Pferdesport/-wetten
- Wir sind flexibel, gehen auf Kundenwünsche immer schnell und kosteneffizient ein
- Unsere softwaretechnischen Fähigkeiten sind ausgezeichnet (wir sind hauptsächlich Programmierer - weniger Businessleute).
- Wir sind für unsere Kunden immer persönlich, direkt und einfach ansprechbar (kleine Firma)
- Wir sind seit ca 15 Jahren erfolgreich im Markt, und auch Marktführer im deutschsprachigen Raum
- Wir haben ein sehr breites Produktportfolio (Terminal, Kassa, Mobile Webseite, Desktop Webseite, Backoffice, Risk Management)
- Wir legen viel Wert auf sauberes und auch modernes UI/UX-Design
Wir benötigen nun einen professionellen Webauftritt um in neue Märkte einzutreten.
Als ersten Schritt möchten wir gerne eine Single-Page Landingpage, die alle wichtigen Punkte im Überblick darstellt.
Aufgabenstellung
Das Design soll die Punkte aus der obigen Beschreibung über uns widerspiegeln, und auch unsere Werte:
Wichtig: Modern, Verlässlichkeit, Dynamisch, Kosteneffizient, Freundlich
Optional: Kreativ, Flexibilität
Wichtig ist auch der Bezug zum Pferderennsport!
Und dass wir eine B2B Softwarefirma sind!
Bitte beachten Sie unser neues Firmenlogo - siehe Anhang.
Die Landingpage soll eher hell, klar, offen, freundlich, sachlich sein.
Die Landingpage soll auf Mobile und Desktop funktionieren und gut aussehen.
Bitte verwenden Sie folgende Gliederung der Landingpage:
Sections:
....* Above the fold
........headline: horse betting software
........subheadline: Multi-product betting solution for bookmakers and racetrack operators.
................................Software production for land-based operations and online betting.
........call-to-action: get in touch
........secondary call-to-action: view products
........switch language
........links to other sections
....* Products
........Point of Sale
............Title: Quick and streamlined bet placement
............Short desc: Optimized bet placement solution for your bet shops and race tracks. Supports Windows-based touchscreen terminals and many different printers and scanners out of the box.
........Self-Service Terminals
............Title: Let users take control
............Short desc: Easy to use touchscreen software for new and professional punters. Running on any Windows-based hardware and adapted to your special needs.
........Web and Mobile Betting
............Title: Reach your target audience wherever they are
............Short desc: Allow your customers to enter their bets on any desktop or mobile browser.
........Bet Management
............Title: Stay in control of your meetings and bets
............Short desc: Browser-based Back-Office solution to control all your meetings,..

```html
<!DOCTYPE html>
<html lang="en">
<head>
<meta charset="utf-8">
<title>brightmoor – Horse Betting Software</title>
<link href="https://fonts.googleapis.com/css2?family=Poppins:wght@400;500;600;700&display=swap" rel="stylesheet">
<style>
:root{
  --nav-bg:#2d2d2d;
  --hero-bg:#f4f4f6;
  --page-bg:#fafafb;
  --accent:#33cbea;
  --navy:#0b4f7e;
  --ink:#1f2a37;
  --text:#3a3f47;
  --white:#ffffff;
  --line:#ececef;
  --screen:#2b3542;
}
*{margin:0;padding:0;box-sizing:border-box}
html,body{width:671px;height:1200px;overflow:hidden}
body{font-family:'Poppins',sans-serif;background:var(--page-bg);position:relative;color:var(--text)}
.abs{position:absolute}
.nav{left:0;top:0;width:671px;height:51px;background:var(--nav-bg)}
.brand{left:85px;top:16px;color:var(--white);font-weight:600;font-size:13px;letter-spacing:1px;line-height:20px}
.nav-link{top:19px;color:var(--white);font-size:7px;line-height:12px}
.contact{left:531px;top:16px;width:44px;height:19px;background:var(--accent);color:var(--white);font-size:7px;border-radius:3px;display:flex;align-items:center;justify-content:center}
.hero{left:0;top:51px;width:671px;height:330px;background:var(--hero-bg)}
.eyebrow{color:var(--accent);font-size:7px;font-weight:600;letter-spacing:.8px;line-height:10px}
.hero-title{left:85px;top:112px;font-size:24px;line-height:28px;font-weight:700;color:var(--ink)}
.hero-copy{left:85px;top:208px;font-size:7.5px;line-height:13.5px;width:220px}
.btn{background:var(--navy);color:var(--white);font-size:7px;font-weight:500;border-radius:3px;display:flex;align-items:center;justify-content:center;box-shadow:0 2px 4px rgba(0,0,0,.18)}
.link{left:190px;top:288px;color:var(--navy);font-size:7px;text-decoration:underline}
.circle{left:340px;top:107px;width:184px;height:184px;border-radius:50%;background:var(--accent)}
.photo{left:326px;top:125px;width:240px;height:168px;border-radius:45% 55% 40% 60%;background:linear-gradient(135deg,#3b3b3b,#8a8a8a 60%,#2a2a2a)}
.phone{left:492px;top:103px;width:28px;height:60px;background:#fff;border-radius:2px;box-shadow:0 1px 4px rgba(0,0,0,.2)}
.terminal{left:420px;top:228px;width:148px;height:80px;background:var(--screen);border-radius:3px;box-shadow:0 2px 6px rgba(0,0,0,.25)}
.center{left:0;width:671px;text-align:center}
.section-title{font-size:21px;font-weight:700;color:var(--ink);line-height:26px}
.section-copy{font-size:7.5px;line-height:13px}
.prod-title{font-size:13px;font-weight:600;color:var(--ink);line-height:16px}
.prod-copy{font-size:7.5px;line-height:12.5px;width:240px}
.feature{height:55px;width:71px;background:var(--white);border-radius:3px;box-shadow:0 1px 4px rgba(0,0,0,.08);display:flex;flex-direction:column;align-items:center;justify-content:center;gap:5px;font-size:7.5px;color:var(--text)}
.shot{border-radius:3px;box-shadow:0 2px 6px rgba(0,0,0,.18)}
.shot.light{background:linear-gradient(180deg,#eef2f6,#dfe5ec)}
.shot.dark{background:var(--screen)}
.shot.green{background:#3e8e3a}
.divider{height:1px;background:var(--line)}
</style>
</head>
<body>
<header class="abs nav">
  <div class="abs brand">brightmoor</div>
  <span class="abs nav-link" style="left:226px">Products</span>
  <span class="abs nav-link" style="left:273px">Why us?</span>
  <span class="abs nav-link" style="left:318px">Company &amp; Team</span>
  <span class="abs nav-link" style="left:396px">FAQ</span>
  <span class="abs nav-link" style="left:482px">DE / EN</span>
  <div class="abs contact">Contact</div>
</header>

<section class="abs hero">
  <div class="abs eyebrow" style="left:85px;top:44px">HORSE BETTING SOFTWARE PROVIDERS</div>
  <h1 class="abs hero-title" style="top:61px">The Reliable Way<br>To Manage<br>Your Horse Races</h1>
  <p class="abs hero-copy" style="top:157px">We provide multi-product betting solutions for bookmakers and racetrack operators.<br>Our proven software products are a perfect fit for land-based as well as online betting operations.</p>
  <div class="abs btn" style="left:85px;top:230px;width:89px;height:23px">View our products</div>
  <span class="abs link" style="top:237px">Get in touch</span>
  <div class="abs circle" style="top:56px"></div>
  <div class="abs photo" style="top:74px" role="img" aria-label="Photo of a racehorse and jockey at full gallop"></div>
  <div class="abs phone" style="top:52px" role="img" aria-label="Mobile betting app screen"></div>
  <div class="abs terminal" style="top:177px" role="img" aria-label="Betting terminal software screen"></div>
</section>

<div class="abs center eyebrow" style="top:429px">BETTING SOLUTIONS</div>
<h2 class="abs center section-title" style="top:446px">Our Products</h2>
<p class="abs center section-copy" style="top:481px">Neque egestas congue quisque egestas diam in. Semper quis<br>lectus nulla at volutpat diam ut venenatis.</p>

<h3 class="abs prod-title" style="left:90px;top:570px">Point of Sale</h3>
<p class="abs prod-copy" style="left:90px;top:598px">Lorem ipsum dolor sit amet, consectetur adipiscing elit, sed do eiusmod tempor incididunt ut labore et dolore magna aliqua.</p>
<div class="abs feature" style="left:94px;top:638px"><svg width="18" height="14"><rect x="4" y="3" width="10" height="10" transform="rotate(45 9 8)" fill="#f2a07b"/><circle cx="10" cy="4" r="3.5" fill="#4cc27a"/></svg>100% reliable</div>
<div class="abs feature" style="left:174px;top:638px"><svg width="18" height="14"><rect x="4" y="4" width="10" height="10" rx="3" fill="#f7a58a"/></svg>Easy to use</div>
<div class="abs feature" style="left:253px;top:638px"><svg width="18" height="14"><path d="M2 13a7 7 0 0 1 14 0" fill="none" stroke="#f4a12b" stroke-width="3"/><path d="M9 13l6-7" stroke="#2b6cb0" stroke-width="2"/></svg>Performant</div>
<div class="abs btn" style="left:90px;top:709px;width:89px;height:23px">More information</div>
<div class="abs shot light" style="left:349px;top:554px;width:224px;height:145px" role="img" aria-label="Back-office software screenshot with race starters table"></div>
<div class="abs shot light" style="left:409px;top:709px;width:36px;height:23px" role="img" aria-label="Thumbnail of back-office screen"></div>
<div class="abs shot dark" style="left:452px;top:709px;width:43px;height:23px" role="img" aria-label="Thumbnail of terminal screen"></div>
<div class="abs shot light" style="left:503px;top:709px;width:11px;height:23px" role="img" aria-label="Thumbnail of mobile screen"></div>
<div class="abs divider" style="left:90px;top:769px;width:490px"></div>

<div class="abs shot dark" style="left:98px;top:841px;width:224px;height:118px" role="img" aria-label="Self-service terminal betting screen"></div>
<div class="abs shot dark" style="left:142px;top:970px;width:43px;height:23px" role="img" aria-label="Thumbnail of terminal screen"></div>
<div class="abs shot light" style="left:193px;top:970px;width:36px;height:23px" role="img" aria-label="Thumbnail of race list screen"></div>
<div class="abs shot green" style="left:236px;top:970px;width:41px;height:23px" role="img" aria-label="Thumbnail of green terminal screen"></div>
<h3 class="abs prod-title" style="left:342px;top:842px">Self-Service Terminals</h3>
<p class="abs prod-copy" style="left:342px;top:870px">Lorem ipsum dolor sit amet, consectetur adipiscing elit, sed do eiusmod tempor incididunt ut labore et dolore magna aliqua.</p>
<div class="abs feature" style="left:346px;top:911px"><svg width="18" height="14"><rect x="4" y="3" width="10" height="10" transform="rotate(45 9 8)" fill="#f2a07b"/><circle cx="10" cy="4" r="3.5" fill="#4cc27a"/></svg>100% reliable</div>
<div class="abs feature" style="left:425px;top:911px"><svg width="18" height="14"><rect x="4" y="4" width="10" height="10" rx="3" fill="#f7a58a"/></svg>Easy to use</div>
<div class="abs feature" style="left:506px;top:911px"><svg width="18" height="14"><path d="M2 13a7 7 0 0 1 14 0" fill="none" stroke="#f4a12b" stroke-width="3"/><path d="M9 13l6-7" stroke="#2b6cb0" stroke-width="2"/></svg>Performant</div>
<div class="abs btn" style="left:342px;top:985px;width:89px;height:23px">More information</div>
<div class="abs divider" style="left:85px;top:1045px;width:490px"></div>
</body>
</html>
```